I need this design by August 8th or 9th!
Looking for a classy, but FUn door hangers for a community outreach "Maple Lantern Funfair." While we are a faith-based organization, we do NOT want this to look religious. I put the DW square blue so you would have a color reference. With grey and orange as an accent color.
Event: Maple Lantern Funfair!
Location: Calloway Pines Estate neighborhood pavilion by the red silo.
Date: Friday, August 17th
Time: 5:30 p.m. to 8:30 p.m.
Free food, while supplies last!
Yummy desserts,
Bounce house,
Raffle,
Games and activities.

Target Market(s)

Families in the neighborhood

Colors
acd136
959595
fbee3d

Requirements
Must have
• Door hanger,

```html
<!DOCTYPE html>
<html lang="en">
<head>
<meta charset="utf-8">
<title>Maple Lantern Funfair – Door Hanger</title>
<link href="https://fonts.googleapis.com/css2?family=Oswald:wght@700&family=Roboto:wght@400;700&family=Montserrat:wght@400&display=swap" rel="stylesheet">
<style>
  :root {
    --page-bg: #ece9e4;
    --sky-top: #fbab33;
    --sky-mid: #f8a02a;
    --sky-low: #e8801a;
    --ink: #150d05;
    --accent-orange: #e8831d;
    --soft-grey: #d6d6d6;
    --white: #ffffff;
    --brand-blue: #4e7385;
  }
  html, body {
    margin: 0;
    width: 1200px;
    height: 1200px;
    overflow: hidden;
    background: var(--page-bg);
  }
  .door-hanger {
    position: absolute;
    left: 364px;
    top: 40px;
    width: 472px;
    height: 1120px;
    background: var(--ink);
    overflow: hidden;
  }
  .hero-photo {
    position: absolute;
    left: 0; top: 0;
    width: 472px;
    height: 540px;
    background: linear-gradient(180deg, var(--sky-top) 0%, var(--sky-mid) 62%, var(--sky-low) 90%, #5a3008 100%);
  }
  .hero-hill {
    position: absolute;
    left: 0; top: 500px;
    width: 472px;
    height: 60px;
  }
  .hanger-cutout {
    position: absolute;
    left: 0; top: 0;
    width: 472px;
    height: 300px;
  }
  .event-title {
    position: absolute;
    left: 0; width: 100%;
    text-align: center;
    font-family: "Oswald", sans-serif;
    font-weight: 700;
    font-size: 46px;
    line-height: 1;
    margin: 0;
    text-transform: uppercase;
  }
  .event-title .line-one { position: absolute; left: 0; width: 100%; top: 530px; color: var(--accent-orange); }
  .event-title .line-two { position: absolute; left: 0; width: 100%; top: 587px; color: var(--soft-grey); }
  .event-details {
    position: absolute;
    left: 0; width: 100%;
    font-family: "Roboto", sans-serif;
    color: var(--white);
    text-align: center;
  }
  .detail-label { color: var(--accent-orange); }
  .detail-date { top: 663px; font-size: 23px; font-weight: 700; }
  .detail-date .detail-label { font-weight: 400; }
  .detail-time { top: 705px; font-size: 23px; }
  .detail-location {
    top: 750px;
    left: 60px; width: 360px;
    text-align: left;
    font-size: 20.5px;
    line-height: 26px;
  }
  .detail-location .indent { display: block; padding-left: 128px; }
  .detail-location .indent-more { display: block; padding-left: 165px; }
  .free-food {
    position: absolute;
    left: 61px; top: 842px;
    font-family: "Oswald", sans-serif;
    font-weight: 700;
    font-size: 56px;
    line-height: 56px;
    text-transform: uppercase;
  }
  .free-food .free { color: var(--accent-orange); display: block; }
  .free-food .food { color: var(--brand-blue); display: block; }
  .free-food .supply-note {
    display: block;
    font-family: "Roboto", sans-serif;
    font-weight: 400;
    font-size: 15px;
    line-height: 20px;
    color: var(--white);
    text-transform: none;
    letter-spacing: -0.3px;
    margin-top: 2px;
  }
  .activity-list {
    position: absolute;
    left: 212px; top: 852px;
    margin: 0; padding: 0;
    list-style: none;
    font-family: "Montserrat", sans-serif;
    font-size: 21px;
    line-height: 32.5px;
    color: var(--white);
  }
  .activity-list li { display: flex; align-items: center; gap: 9px; }
  .activity-list svg { width: 13px; height: 13px; flex: none; }
  .brand-band {
    position: absolute;
    left: 0; top: 1015px;
    width: 472px;
    height: 105px;
  }
  .brand-tag {
    position: absolute;
    left: 0; width: 100%;
    top: 1045px;
    text-align: center;
    font-family: "Roboto", sans-serif;
    font-weight: 400;
    font-size: 30px;
    color: var(--white);
  }
</style>
</head>
<body>
  <main class="door-hanger">
    <div class="hero-photo" role="img" aria-label="Photo of a group of friends in silhouette holding hands up on a hilltop at sunset"></div>
    <svg class="hero-hill" viewBox="0 0 472 60" preserveAspectRatio="none" aria-hidden="true">
      <path d="M0 28 Q236 -6 472 28 L472 60 L0 60 Z" fill="#150d05"/>
    </svg>
    <svg class="hanger-cutout" viewBox="0 0 472 300" aria-hidden="true">
      <path d="M111 0 L160 0 L205 95 A94 94 0 1 1 180 100 Z" fill="#ece9e4"/>
    </svg>

    <h1 class="event-title">
      <span class="line-one">Maple Lantern</span>
      <span class="line-two">Funfair</span>
    </h1>

    <p class="event-details detail-date" style="margin:0"><span class="detail-label">DATE:</span> Friday, August 17th</p>
    <p class="event-details detail-time" style="margin:0"><span class="detail-label">Time:</span> 5:30 p.m. to 8:30 p.m.</p>
    <p class="event-details detail-location" style="margin:0">
      <span class="detail-label">LOCATION:</span> Calloway Pines Estate
      <span class="indent">neighborhood pavilion</span>
      <span class="indent-more">by the red silo.</span>
    </p>

    <div class="free-food">
      <span class="free">Free</span>
      <span class="food">Food</span>
      <span class="supply-note">while supplies last!</span>
    </div>

    <ul class="activity-list">
      <li><svg viewBox="0 0 14 14"><circle cx="7" cy="7" r="7" fill="#e8831d"/><path d="M3.8 7.2 L6 9.3 L10.2 4.9" fill="none" stroke="#150d05" stroke-width="1.8"/></svg>Yummy desserts</li>
      <li><svg viewBox="0 0 14 14"><circle cx="7" cy="7" r="7" fill="#e8831d"/><path d="M3.8 7.2 L6 9.3 L10.2 4.9" fill="none" stroke="#150d05" stroke-width="1.8"/></svg>Bouncy house</li>
      <li><svg viewBox="0 0 14 14"><circle cx="7" cy="7" r="7" fill="#e8831d"/><path d="M3.8 7.2 L6 9.3 L10.2 4.9" fill="none" stroke="#150d05" stroke-width="1.8"/></svg>Raffle</li>
      <li><svg viewBox="0 0 14 14"><circle cx="7" cy="7" r="7" fill="#e8831d"/><path d="M3.8 7.2 L6 9.3 L10.2 4.9" fill="none" stroke="#150d05" stroke-width="1.8"/></svg>Games &amp; activities</li>
    </ul>

    <svg class="brand-band" viewBox="0 0 472 105" preserveAspectRatio="none" aria-hidden="true">
      <path d="M0 27 Q236 -12 472 27 L472 105 L0 105 Z" fill="#e8831d"/>
      <path d="M0 33 Q236 -4 472 33 L472 105 L0 105 Z" fill="#ffffff"/>
      <path d="M0 36 Q236 0 472 36 L472 105 L0 105 Z" fill="#4e7385"/>
    </svg>
    <p class="brand-tag" style="margin:0">#ForHollowbrook</p>
  </main>
</body>
</html>
```